Marketing Brochure - Conjunction event

We need a brochure for clients/conjunction real estate agents to view the type of projects VARO531 have available.
As a guideline of our requirements, please refer to our company profile. As you can see it is a simple elegant professional image we are after.
We are a Real Estate company specialise in off the plans project marketing. We have sale teams to sell the projects/ residential properties but also conjunction with other real estate agents. This is the first time we decided to use QuillMarket to design our brochure. If pleasing results, ongoing we will have many more design projects to do.

Target Market(s)

Clients / real estate agents

Industry/Entity Type

Real Estate

Font styles to use
Sans Serif

Colors
ffffff
ef484e

Requirements
Must have
• All the details in the documents, Encourage creative designs.
• Company logo and the black banner as seen on company profile brochure
Nice to have
• similar to our company profile brochure( file attached)
Should not have
• Funky or too loud type image

```html
<!DOCTYPE html>
<html lang="en">
<head>
<meta charset="utf-8">
<title>Projects to Sell – Sydney</title>
<link href="https://fonts.googleapis.com/css2?family=Montserrat:wght@800&display=swap" rel="stylesheet">
<style>
  :root {
    --cover-dark: #2b2624;
    --panel-white: #ffffff;
    --ink-dark: #231f1e;
  }
  html, body {
    margin: 0;
    padding: 0;
    width: 848px;
    height: 1200px;
    overflow: hidden;
    background: var(--cover-dark);
  }
  .cover {
    position: relative;
    width: 848px;
    height: 1200px;
    overflow: hidden;
    font-family: "Montserrat", sans-serif;
  }
  .cover-texture {
    position: absolute;
    inset: 0;
    background: var(--cover-dark);
  }
  .title-block {
    position: absolute;
    left: 90px;
    top: 746px;
    width: 500px;
  }
  .title-heading {
    margin: 0 0 0 49px;
    padding-top: 72px;
    color: var(--panel-white);
    font-weight: 800;
    font-size: 46px;
    line-height: 63px;
    letter-spacing: 0.5px;
    text-transform: uppercase;
  }
  .title-rule {
    height: 4px;
    width: 120px;
    margin: 26px 0 0 49px;
    background: var(--panel-white);
  }
  .city-bar {
    margin-top: 22px;
    height: 114px;
    background: var(--panel-white);
  }
  .city-name {
    margin: 0;
    padding: 5px 0 0 41px;
    color: var(--ink-dark);
    font-weight: 800;
    font-size: 88px;
    line-height: 104px;
    letter-spacing: 0.5px;
    text-transform: uppercase;
  }
</style>
</head>
<body>
  <main class="cover">
    <div class="cover-texture" role="img" aria-label="Subtle dark dotted background texture"></div>

    <section class="title-block">
      <h1 class="title-heading">Projects<br>to sell</h1>
      <div class="title-rule"></div>
      <div class="city-bar">
        <p class="city-name">Sydney</p>
      </div>
    </section>
  </main>
</body>
</html>
```